Dietitian needs awesome business card

I need a contemporary design that's eye catching but professional.
My card is to given to doctors, specialists and patients alike.
I manage patients with chronic diseases
I have uploaded my logo and current business card, I would also like the other Registered Clinical Nutritionist logo incorporated into the design

Target Market(s)

Doctors, specialists and patients

Industry/Entity Type

Healthcare

Contact Information for Business Card

www.brindlecovenutrition.com.au
Ph: 0427 516 903
Fax: 6482 7315
email: marcus.k.wellfare@quorvamail.com
Space on the back of the card with: Appointment date, Appointment time and appointment location

Font styles to use
Serif

Colors
fbee3e
876aae
ffc214

Requirements
Must have
• My Logo
• Registered Clinical Nutritionist Logo
• My 4 locations - Fernhollow Medical Centre, North Kelby Health, Ashcourt Medical, Pinebrook Doctors Surgery
Nice to have
• I like the colours in my current business card

```html
<!DOCTYPE html>
<html lang="en">
<head>
<meta charset="utf-8">
<title>Brindle Cove Nutrition – Business Card</title>
<link href="https://fonts.googleapis.com/css2?family=Cabin:wght@400;600;700&family=Noto+Serif:wght@400&family=Open+Sans:wght@300;400&display=swap" rel="stylesheet">
<style>
  :root {
    --page-bg: #e9e9e7;
    --card-bg: #ffffff;
    --leaf-green: #5fb336;
    --leaf-green-light: #8cc63f;
    --ocean-blue: #1f63ad;
    --badge-orange: #f27a1f;
    --ink-grey: #555a5e;
    --rule-grey: #a6a8aa;
    --soft-grey: #7b7f82;
  }
  * { box-sizing: border-box; margin: 0; padding: 0; }
  html, body {
    width: 1200px; height: 1023px; overflow: hidden;
    background: var(--page-bg);
  }
  .sheet {
    width: 1200px; height: 1023px;
    display: flex; flex-direction: column; align-items: center; justify-content: center;
    gap: 50px;
  }
  .card {
    position: relative;
    width: 760px; height: 434px;
    background: var(--card-bg);
    box-shadow: 0 6px 18px rgba(0,0,0,.18);
    overflow: hidden;
  }

  /* Front */
  .card-front .side-band {
    position: absolute; left: 0; top: 0; bottom: 0; width: 62px;
    background: linear-gradient(180deg, var(--leaf-green-light), var(--leaf-green));
  }
  .brand {
    position: absolute; left: 96px; top: 44px;
    display: flex; align-items: center; gap: 14px;
  }
  .brand-dot {
    width: 46px; height: 46px; border-radius: 50%;
    background: var(--ocean-blue); flex: none;
  }
  .brand-name {
    font-family: "Cabin", sans-serif; font-weight: 600;
    font-size: 26px; color: var(--ocean-blue); white-space: nowrap;
  }
  .locations {
    position: absolute; left: 96px; top: 136px; list-style: none;
  }
  .locations li {
    font-family: "Open Sans", sans-serif; font-weight: 400;
    font-size: 15px; color: var(--ink-grey); line-height: 26px;
  }
  .contact {
    position: absolute; right: 56px; top: 120px; text-align: right;
  }
  .contact-name {
    font-family: "Cabin", sans-serif; font-weight: 400;
    font-size: 40px; line-height: 48px; color: var(--leaf-green);
  }
  .contact-role {
    font-family: "Open Sans", sans-serif; font-weight: 400;
    font-size: 15px; color: var(--ink-grey); margin-bottom: 16px;
  }
  .contact-line {
    font-family: "Open Sans", sans-serif; font-weight: 300;
    font-size: 18px; color: var(--soft-grey); line-height: 29px;
  }
  .accreditation-badge {
    position: absolute; left: 96px; bottom: 40px;
    width: 74px; height: 74px; background: var(--badge-orange);
  }

  /* Back */
  .appointment-title {
    position: absolute; left: 430px; top: 50px;
    font-family: "Noto Serif", serif; font-weight: 400; font-size: 34px; color: var(--ink-grey);
  }
  .appointment-fields {
    position: absolute; left: 430px; top: 140px; width: 290px;
    display: flex; flex-direction: column; gap: 42px;
  }
  .field { display: flex; align-items: flex-end; gap: 14px; }
  .field-label {
    font-family: "Cabin", sans-serif; font-weight: 700;
    font-size: 24px; color: var(--leaf-green); width: 72px;
  }
  .field-rule { flex: 1; border-bottom: 2px solid var(--rule-grey); margin-bottom: 7px; }
  .back-brand {
    position: absolute; left: 48px; bottom: 60px;
    display: flex; align-items: center; gap: 14px;
  }
  .back-brand .brand-dot { width: 64px; height: 64px; }
  .back-brand .brand-name { font-size: 26px; }
  .bottom-band {
    position: absolute; left: 0; right: 0; bottom: 0; height: 16px;
    background: linear-gradient(90deg, var(--ocean-blue), var(--leaf-green));
  }
</style>
</head>
<body>
<main class="sheet">
  <section class="card card-front" aria-label="Card front">
    <div class="side-band"></div>
    <div class="brand">
      <span class="brand-dot"></span>
      <span class="brand-name">Brindle Cove Nutrition</span>
    </div>
    <ul class="locations">
      <li>Fernhollow Medical Centre</li>
      <li>North Kelby Health</li>
      <li>Ashcourt Medical</li>
      <li>Pinebrook Doctors Surgery</li>
    </ul>
    <div class="contact">
      <p class="contact-name">Marcus Wellfare</p>
      <p class="contact-role">Registered Clinical Nutritionist</p>
      <p class="contact-line">Ph: 0427 516 903</p>
      <p class="contact-line">Fax: 6482 7315</p>
      <p class="contact-line">marcus.k.wellfare@quorvamail.com</p>
      <p class="contact-line">www.brindlecovenutrition.com.au</p>
    </div>
    <div class="accreditation-badge"></div>
  </section>

  <section class="card card-back" aria-label="Card back">
    <h1 class="appointment-title">Appointment</h1>
    <div class="appointment-fields">
      <div class="field"><span class="field-label">Time</span><span class="field-rule"></span></div>
      <div class="field"><span class="field-label">Date</span><span class="field-rule"></span></div>
      <div class="field"><span class="field-label">Place</span><span class="field-rule"></span></div>
    </div>
    <div class="back-brand">
      <span class="brand-dot"></span>
      <span class="brand-name">Brindle Cove Nutrition</span>
    </div>
    <div class="bottom-band"></div>
  </section>
</main>
</body>
</html>
```